Mend ORX Syndrome (Non-Profit) Tri-Fold Brochure Design

We have put together the content for a brochure that we will distribute to doctors, researchers and patients about our non-profit. We would like the design of the brochure to look more professional and have nice aesthetics. It needs to incorporate all of the content in the attached Word file. We will have printed once we have a finished design.

Target Market(s)

Medical

Industry/Entity Type

Non Profit

Font styles to use
Serif
Sans Serif

Colors
33a6d7

Requirements
Must have
• Must include all content provided. Professional.
Nice to have
• Colors

```html
<!DOCTYPE html>
<html lang="en">
<head>
<meta charset="utf-8">
<title>Mend ORX Syndrome — Tri-Fold Brochure</title>
<link href="https://fonts.googleapis.com/css2?family=Montserrat:wght@400;600;700;800&family=Oswald:wght@500&family=Roboto:wght@300;400;500&display=swap" rel="stylesheet">
<style>
:root{
  --stage:#1f5870;
  --label:#8fa4b4;
  --blue:#33a6d7;
  --deep:#2a8ec4;
  --teal:#2fb3b8;
  --teal-dark:#1f9aa3;
  --ink:#444;
  --paper:#ffffff;
  --mist:#eef4f7;
}
*{box-sizing:border-box;margin:0;padding:0}
html,body{width:900px;height:1200px;overflow:hidden}
body{background:var(--stage);font-family:"Roboto",sans-serif;color:var(--ink);position:relative}
.fold-label{position:absolute;left:30px;font-family:"Oswald",sans-serif;font-weight:500;font-size:40px;letter-spacing:1px;color:var(--label)}
.fold-label.outside{top:1140px;left:auto;right:30px}
.spread{position:absolute;left:30px;width:840px;height:520px;display:flex;background:var(--paper);box-shadow:0 12px 30px rgba(0,0,0,.35)}
.spread.inside{top:70px}
.spread.outside{top:605px}
.panel{position:relative;width:280px;height:520px;overflow:hidden;background:var(--paper)}
.panel + .panel{border-left:1px solid #e3e9ec}
.abs{position:absolute}
h2{font-family:"Montserrat",sans-serif;font-weight:800;font-size:15px;color:var(--teal);text-transform:uppercase;display:flex;align-items:center;gap:6px}
h2 .rule{flex:1;height:1px;background:currentColor;max-width:70px}
h3{font-family:"Montserrat",sans-serif;font-weight:700;font-size:10px;color:var(--deep);text-transform:uppercase;line-height:1.05}
h3 small{display:block;font-weight:400;font-size:10px;color:var(--blue)}
p{font-size:8.2px;line-height:1.4}
.symptom{display:flex;gap:9px;margin-bottom:11px}
.symptom .icon{flex:0 0 30px;height:22px;background:var(--deep);border-radius:2px;margin-top:2px}
.symptom p{margin-top:3px}
.photo{position:absolute;background:linear-gradient(135deg,#b8cfd8,#7fa7b6 55%,#5d8a9c)}
.dna{flex:0 0 14px;width:14px;height:26px;background:linear-gradient(var(--blue),var(--teal));border-radius:7px;opacity:.8}
.callout{font-family:"Montserrat",sans-serif;font-weight:700;font-size:10px;color:var(--deep);text-transform:uppercase;text-align:center;line-height:1.45}
.webbox{border:1px solid var(--deep);padding:6px;text-align:center;font-size:8.5px;color:var(--blue)}
.webbox strong{display:block;font-family:"Montserrat",sans-serif;font-size:11px;color:var(--deep)}
ul.plain{list-style:none}
ul.plain li{font-size:8.2px;line-height:1.4;padding-left:10px;position:relative;margin-bottom:4px}
ul.plain li::before{content:"";position:absolute;left:0;top:4px;width:5px;height:5px;background:var(--deep)}
.on-blue{color:#fff}
.on-blue h2{color:#fff}
.penetrance ul.plain li{font-size:9px;margin-bottom:2px}
.penetrance ul.plain li::before{background:#fff}
.contact li{display:flex;gap:8px;align-items:flex-start;font-size:8.5px;line-height:1.35;margin-bottom:7px;list-style:none}
.contact svg{flex:0 0 10px;margin-top:1px}
.brand-name{font-family:"Montserrat",sans-serif;font-weight:700;font-size:14px;color:var(--deep);display:flex;align-items:center;gap:6px}
.brand-name .dot{width:12px;height:12px;border-radius:50%;background:var(--deep)}
.question{font-family:"Montserrat",sans-serif;font-weight:700;font-size:10px;color:#fff;line-height:1.5;text-transform:uppercase}
.pie-labels text{font-family:"Roboto",sans-serif;font-size:6.5px;fill:#fff}
</style>
</head>
<body>

<div class="fold-label">INSIDE FOLD</div>

<section class="spread inside">

  <div class="panel symptoms">
    <svg class="abs" style="left:0;top:0" width="280" height="100" viewBox="0 0 280 100" aria-hidden="true">
      <path d="M0 0H280V70Q150 100 0 82Z" fill="var(--teal)"/>
    </svg>
    <div class="abs on-blue" style="left:18px;top:18px;width:245px">
      <h2>Symptoms <span class="rule"></span></h2>
      <p style="margin-top:4px">IBMPFD, a ORX Disease, is an adult onset disorder that can affect the muscles, bones, and brain, and an affected patient may have any combination of the following conditions:</p>
    </div>
    <div class="abs" style="left:18px;top:108px;width:248px">
      <div class="symptom"><div class="icon" role="img" aria-label="Muscle icon"></div><div>
        <h3>Inclusion <small>Body Myopathy</small></h3>
        <p>The first symptom of IBMPFD is often muscle weakness (myopathy). Typically, patients first notice difficulty raising arms, losing balance or difficulty climbing stairs. As the disorder progresses, weakness develops in the other muscles in the arms, legs and core muscles. Muscle weakness can also affect respiratory and heart (cardiac) muscles. This disorder may first present in an individual's late 30's and over time occurs in approximately 90% of individuals with ORX Disease.</p></div></div>
      <div class="symptom"><div class="icon" role="img" aria-label="Bone icon"></div><div>
        <h3>Paget's Disease <small>of Bone</small></h3>
        <p>Bone pain, particularly in the hips and spine, is usually the major symptom of Paget's disease. It most often affects bones of the hips, spine, and skull, and the long bones of the arms and legs. Paget's disease affects half of individuals with ORX Disease and typically first presents in a person's 30's or 40's, which is a much earlier age than those without ORX Disease.</p></div></div>
      <div class="symptom"><div class="icon" role="img" aria-label="Brain icon"></div><div>
        <h3>Frontotemporal <small>Dementia</small></h3>
        <p>In about one-third of people with ORX Disease, the disorder also affects the brain. FTD typically changes personality, behavior, language and speech. FTD typically presents in the mid-50's.</p></div></div>
      <div class="symptom"><div class="icon" role="img" aria-label="Nerve cell icon"></div><div>
        <h3>Amyotrophic Lateral Sclerosis <small>(ALS or Lou Gehrig's Disease)</small></h3>
        <p>ALS occurs in approximately 10% of individuals with ORX Disease. Symptoms include increased muscle tone, weakness, muscle wasting, muscle cramps, difficulty swallowing and speaking.</p></div></div>
    </div>
  </div>

  <div class="panel research">
    <div class="photo" style="left:0;top:0;width:280px;height:110px" role="img" aria-label="Photo of a smiling doctor in a hospital corridor"></div>
    <svg class="abs" style="left:0;top:0" width="280" height="130" viewBox="0 0 280 130" aria-hidden="true">
      <path d="M0 0H170L140 80Q70 95 0 60Z" fill="var(--teal)" opacity=".82"/>
      <path d="M0 110Q140 85 280 100V130H0Z" fill="var(--paper)"/>
    </svg>
    <div class="abs" style="left:18px;top:14px;width:140px;font-family:Montserrat,sans-serif;font-weight:700;font-size:11px;line-height:1.45;color:#fff;text-transform:uppercase">Strength through numbers will help us find a cure!</div>
    <div class="abs" style="left:18px;top:122px;width:245px">
      <h2 style="color:var(--deep)"><span class="dna" role="img" aria-label="DNA icon"></span>Research <span class="rule"></span></h2>
      <p style="margin:5px 0 12px 20px">The goal of the KinRare registry is to connect as many patients and researchers as possible to help advance treatments and cures for rare diseases.</p>
      <div class="callout">If you have been diagnosed with IBMPFD or ORX disease, please help us by completing the patient registry through KinRare.</div>
      <div class="webbox" style="margin:11px 10px">Go to our website<strong>www.mendorx.org</strong>to access the KinRare Registry.</div>
      <p style="margin-bottom:6px">The KinRare registry is free for patients to enroll and for researchers to access.</p>
      <p>Please elect for researchers to have access to your registry, as that will greatly assist in the drive for a cure, especially when drug trials are recruiting patients.</p>
    </div>
    <div class="abs" style="left:0;top:466px;width:280px;height:54px;background:var(--mist)"></div>
    <div class="abs" style="left:18px;top:478px;font-family:Montserrat,sans-serif;font-weight:700;font-size:11px;color:var(--deep)">KinRare Registry</div>
    <div class="photo" style="left:160px;top:470px;width:110px;height:46px;border-radius:50% 50% 0 0;background:linear-gradient(160deg,#dfe9ee,#9db8c6)" role="img" aria-label="Illustration of a globe"></div>
  </div>

  <div class="panel diagnosis">
    <svg class="abs" style="left:0;top:0" width="280" height="520" viewBox="0 0 280 520" aria-hidden="true">
      <path d="M150 0H280V90Q230 30 150 0Z" fill="var(--teal)" opacity=".5"/>
      <path d="M200 0H280V60Q250 20 200 0Z" fill="var(--deep)"/>
      <path d="M0 470Q150 430 280 440V520H0Z" fill="var(--teal)"/>
      <path d="M0 490Q150 455 280 470V520H0Z" fill="var(--deep)"/>
    </svg>
    <div class="abs" style="left:18px;top:50px;width:245px">
      <h2 style="color:var(--deep)"><span class="dna" role="img" aria-label="DNA icon"></span>Diagnosis <span class="rule"></span></h2>
      <p style="margin:5px 0 8px 20px">The only way of diagnosing ORX Disease is through genetic testing. Consult with your doctor about testing for mutations of the ORX gene.</p>
      <p style="margin:0 0 8px 20px">For information about genetic testing, our two medical advisors are available as resources:</p>
      <ul class="plain" style="margin-left:20px">
        <li>Dr. Lena Marsh, Medical Geneticist at West Coast University, lmarsh@westcoastu.edu</li>
        <li>Dr. Paul Ardent, Neuromuscular Specialist at Midland University, ardentp@midlandu.edu</li>
      </ul>
      <h2 style="color:var(--deep);margin-top:26px"><span class="dna" role="img" aria-label="DNA icon"></span>Treatments <span class="rule"></span></h2>
      <p style="margin:5px 0 8px 20px">There is an approved treatment for Paget's disease of bone, so early testing for this disorder is very important.</p>
      <p style="margin-left:20px">There are no known cures or treatments for the Inclusion Body Myopathy or Frontotemporal Dementia. Consult with your doctor about physical therapy, stretching, diet and mobility aids.</p>
    </div>
  </div>
</section>

<section class="spread outside">

  <div class="panel what-is">
    <div class="photo" style="left:0;top:250px;width:280px;height:270px;background:linear-gradient(160deg,#5fb4dc,var(--deep))" role="img" aria-label="Faint photo of a doctor with a patient"></div>
    <svg class="abs" style="left:0;top:0" width="280" height="520" viewBox="0 0 280 520" aria-hidden="true">
      <path d="M0 0H280V240Q140 290 0 255Z" fill="var(--paper)"/>
      <path d="M0 480Q140 455 280 468V520H0Z" fill="var(--teal)"/>
    </svg>
    <div class="abs" style="left:18px;top:40px;width:245px">
      <h2 style="color:var(--deep);display:block">What is<span style="display:block;font-weight:400;font-size:14px;color:var(--blue)">IBMPFD?</span></h2>
      <p style="margin:6px 0">Inclusion Body Myopathy associated with Paget's disease of Bone and Frontotemporal Dementia is an autosomal dominant mutation in chromosome 9 of the ORX (Valosin Containing Protein) gene. Given the interaction with other genetic diseases, this mutation may also be known as ORX Disease or Disorder.</p>
      <p>Some patients have familial Amyotrophic Lateral Sclerosis (ALS or Lou Gehrig's disease) or Parkinson's which has been shown to have a pathogenic variant in ORX.</p>
    </div>
    <div class="abs on-blue penetrance" style="left:18px;top:282px;width:245px">
      <h2 style="display:block">Penetrance<span style="display:block;font-weight:400;font-size:13px">by phenotype</span></h2>
      <p style="margin:4px 0 5px;font-size:9px">The frequency that IBMPFD or ORX Disease manifests itself in one, two, or three primary disorders.</p>
      <ul class="plain">
        <li>IBM: Inclusion Body Myopathy</li>
        <li>PDB: Paget's Disease of the Bone</li>
        <li>FTD: Frontotemporal Dementia</li>
      </ul>
    </div>
    <svg class="abs" style="left:18px;top:410px" width="244" height="106" viewBox="0 0 244 106" role="img" aria-label="Pie chart of penetrance by phenotype">
      <g transform="translate(122 56) rotate(-90) scale(1.15)">
        <circle r="15.915" fill="none" stroke="#9a9a9a" stroke-width="31.83" stroke-dasharray="37 63"/>
        <circle r="15.915" fill="none" stroke="#f5b21c" stroke-width="31.83" stroke-dasharray="27 73" stroke-dashoffset="-37"/>
        <circle r="15.915" fill="none" stroke="#f07f2d" stroke-width="31.83" stroke-dasharray="16 84" stroke-dashoffset="-64"/>
        <circle r="15.915" fill="none" stroke="#3f63b5" stroke-width="31.83" stroke-dasharray="10 90" stroke-dashoffset="-80"/>
        <circle r="15.915" fill="none" stroke="#6aa84f" stroke-width="31.83" stroke-dasharray="5 95" stroke-dashoffset="-90"/>
        <circle r="15.915" fill="none" stroke="#5a8fd6" stroke-width="31.83" stroke-dasharray="3 97" stroke-dashoffset="-95"/>
        <circle r="15.915" fill="none" stroke="#c0392b" stroke-width="31.83" stroke-dasharray="2 98" stroke-dashoffset="-98"/>
      </g>
      <g class="pie-labels">
        <text x="166" y="58">IBM - 37%</text>
        <text x="76" y="98" text-anchor="end">IBM &amp; PDB - 27%</text>
        <text x="76" y="70" text-anchor="end">IBM &amp; FTD - 16%</text>
        <text x="76" y="48" text-anchor="end">IBM, PDB &amp; FTD - 10%</text>
        <text x="76" y="36" text-anchor="end">PDB - 5%</text>
        <text x="76" y="26" text-anchor="end">FTD - 3%</text>
        <text x="76" y="16" text-anchor="end">PDB &amp; FTD - 1%</text>
      </g>
    </svg>
  </div>

  <div class="panel together">
    <svg class="abs" style="left:0;top:0" width="280" height="520" viewBox="0 0 280 520" aria-hidden="true">
      <rect width="280" height="520" fill="var(--deep)"/>
      <path d="M0 0H280V185Q140 160 0 190Z" fill="var(--paper)"/>
      <path d="M0 440Q140 470 280 420V520H0Z" fill="var(--teal)"/>
      <path d="M0 470Q140 500 280 450V520H0Z" fill="var(--teal-dark)"/>
    </svg>
    <div class="abs" style="left:18px;top:40px;width:245px">
      <h2 style="color:var(--deep);display:block">Together we can<span style="display:block;font-weight:400;font-size:12px;color:var(--blue);text-transform:none">Make a Difference</span></h2>
      <div style="font-family:Montserrat,sans-serif;font-size:8.5px;color:var(--deep);text-transform:uppercase;margin:8px 0 4px">Patient Support</div>
      <p>Mend ORX Syndrome, Inc. is a 501(c)(3) which was formed to drive efforts to cure diseases related to mutations of the Valosin Containing Protein (ORX) gene. Our main goal is to bring patients and doctors together so we can help one another and drive research towards a cure. We are also trying to bring awareness to the medical community about our rare disease.</p>
    </div>
    <div class="abs on-blue" style="left:18px;top:220px;width:245px">
      <div style="font-family:Montserrat,sans-serif;font-weight:700;font-size:11px">WE OFFER</div>
      <p style="font-size:9.5px;margin:3px 0 22px">Resources and Support to patients, caregivers and doctors.</p>
      <div style="font-family:Montserrat,sans-serif;font-weight:700;font-size:11px;margin-bottom:8px">CONNECT WITH US</div>
      <ul class="contact">
        <li><svg width="10" height="12" viewBox="0 0 10 12"><path d="M5 0a4 4 0 0 0-4 4c0 3 4 8 4 8s4-5 4-8a4 4 0 0 0-4-4zm0 5.5a1.5 1.5 0 1 1 0-3 1.5 1.5 0 0 1 0 3z" fill="#fff"/></svg>Mend ORX Syndrome, Inc. P.O. Box 4120<br>Lindale, OR 97001</li>
        <li><svg width="10" height="8" viewBox="0 0 10 8"><rect width="10" height="8" fill="#fff"/><path d="M0 0l5 4 5-4" stroke="var(--deep)" fill="none"/></svg>mendorxsyndrome@mail.org</li>
        <li><svg width="10" height="10" viewBox="0 0 10 10"><circle cx="5" cy="5" r="4.3" fill="none" stroke="#fff"/><path d="M1 5h8M5 1v8" stroke="#fff"/></svg>www.mendorx.org<br>orxinfo.org</li>
        <li><svg width="10" height="10" viewBox="0 0 10 10"><circle cx="5" cy="5" r="5" fill="#fff"/></svg>ORXSupport</li>
      </ul>
    </div>
    <div class="abs" style="left:40px;top:446px;width:110px;height:34px;background:#fff;border-radius:3px" role="img" aria-label="Member badge"></div>
  </div>

  <div class="panel cover">
    <div class="photo" style="left:0;top:0;width:280px;height:200px;background:linear-gradient(150deg,#e8eff3,#a9c3cf 60%,#7b9fae)" role="img" aria-label="Photo of a doctor holding a stethoscope"></div>
    <svg class="abs" style="left:0;top:0" width="280" height="520" viewBox="0 0 280 520" aria-hidden="true">
      <path d="M0 150L280 95V155L0 215Z" fill="var(--teal)" opacity=".85"/>
      <path d="M0 200L280 140V250Q140 300 0 320Z" fill="var(--deep)"/>
      <path d="M0 470Q140 440 280 455V520H0Z" fill="var(--teal)"/>
    </svg>
    <div class="abs" style="left:16px;top:18px;background:rgba(255,255,255,.92);padding:8px 10px">
      <div class="brand-name"><span class="dot"></span>Mend ORX Syndrome</div>
    </div>
    <div class="abs" style="right:16px;top:120px;width:130px;text-align:right;font-family:Montserrat,sans-serif;font-weight:700;font-size:10px;line-height:1.35;color:#fff">Do you have a family history of ADULT ONSET</div>
    <div class="abs" style="left:18px;top:215px;width:200px">
      <div class="question">Muscle weakness?<br>Dementia?<br>Bone disease?<br>ALS?<br>Parkinson's?<br>IBM?</div>
    </div>
    <div class="abs" style="right:18px;top:340px;width:170px;text-align:right">
      <p style="font-size:9.5px">You may consider talking to your doctor about a mutation of the ORX gene called</p>
      <div style="font-family:Montserrat,sans-serif;font-weight:800;font-size:20px;color:var(--deep);margin-top:4px">IBMPFD</div>
      <p style="font-size:9px;color:var(--teal-dark);margin-top:3px">Inclusion Body Myopathy associated with Paget's Disease of Bone and Frontotemporal Dementia.</p>
    </div>
  </div>
</section>

<div class="fold-label outside">OUTSIDE FOLD</div>

</body>
</html>
```